New Email Marketing Design Project

We need an email signature to highlight our brand, as well as include our product ranges. The brand has an Italian origin and we have a logo developed already.
For the email signature please include the following content:
Dean Orsk | Partner
Email: Dean.orsk@vetrascan.com.au
Office: + 61 2 9481 7062
Mobile: + 61 438 915 264
Web: www.vetrascan.com.au

Vetrascan Lifestyle Centre:
Level 2, Brackenfold Design Centre
84 Tarrant Street, Waterloo
NSW 2043 Australia

[Product ranges] Kitchen Appliances | Designer Joineries | Blinds & Curtains | Fire Places | Featured Lightings | Smart Home | Bathroom Products

```html
<!DOCTYPE html>
<html lang="en">
<head>
<meta charset="utf-8">
<title>Vetrascan – New Arrival Sale</title>
<link rel="stylesheet" href="https://fonts.googleapis.com/css2?family=Roboto:wght@300;400;500;700;900&family=Tinos:wght@700&display=swap">
<style>
  :root {
    --page: #ffffff;
    --panel: #f8f8f8;
    --ink: #111111;
    --text: #222222;
    --muted: #555555;
    --green: #1a8a44;
    --red: #b01e3a;
    --white: #ffffff;
    --hero-light: #e4ddd6;
    --hero-dark: #8a7a6c;
    --room-wood: #8c6d44;
    --room-dark: #24292a;
    --room-floor: #e6e9ea;
    --lounge-dark: #2a2523;
    --lounge-wood: #5a3f2e;
    --social: #9aa3ad;
  }
  * { box-sizing: border-box; margin: 0; padding: 0; }
  html, body {
    width: 700px; height: 1200px; overflow: hidden;
    background: var(--page);
    font-family: "Roboto", Arial, sans-serif;
    color: var(--text);
  }
  .email {
    position: absolute; left: 195.7px; top: 55.6px;
    width: 600px; height: 2114px;
    background: var(--panel);
    transform: scale(0.5147); transform-origin: 0 0;
    text-align: center;
  }
  .masthead { height: 89px; display: flex; align-items: center; justify-content: center; }
  .brand-name {
    font-family: "Roboto", Arial, sans-serif; font-weight: 900;
    font-size: 46px; letter-spacing: 1px; color: var(--ink);
  }
  .hero {
    position: relative; height: 279px;
    background: linear-gradient(180deg, var(--hero-light) 0%, #d8cfc6 62%, var(--hero-dark) 100%);
  }
  .hero-copy { position: absolute; inset: 0; }
  .hero-kicker { position: absolute; top: 37px; width: 100%; font-size: 15px; font-weight: 400; color: var(--ink); }
  .hero-title { position: absolute; top: 74px; width: 100%; font-size: 58px; font-weight: 900; color: var(--ink); line-height: 1; }
  .hero-offer { position: absolute; top: 154px; width: 100%; font-size: 15px; font-weight: 500; color: var(--ink); }
  .hero-offer em { font-style: normal; color: var(--red); font-size: 18px; }
  .hero .btn { position: absolute; top: 198px; left: 224px; width: 152px; height: 40px; }
  .btn {
    display: inline-flex; align-items: center; justify-content: center;
    background: var(--green); color: var(--white);
    font-size: 15px; font-weight: 700; letter-spacing: 2px; text-decoration: none;
  }
  .intro { padding-top: 17px; }
  .section-title { font-size: 22px; font-weight: 500; color: var(--ink); line-height: 26px; }
  .intro p { width: 510px; margin: 17px auto 0; font-size: 14px; line-height: 22px; font-weight: 300; color: var(--ink); }
  .products { display: grid; grid-template-columns: 267px 267px; column-gap: 12px; row-gap: 52px; padding: 48px 27px 0; }
  .product-photo { height: 178px; background: linear-gradient(180deg, var(--room-wood) 0%, #6d5a3e 18%, var(--room-dark) 30%, #3a4143 58%, var(--room-floor) 78%, #f2f4f5 100%); }
  .product h3 { margin-top: 19px; font-size: 19px; font-weight: 500; color: var(--ink); line-height: 24px; }
  .product p { width: 240px; margin: 17px auto 0; font-size: 14px; line-height: 22px; font-weight: 300; color: var(--ink); }
  .price { margin-top: 14px; font-size: 18px; font-weight: 700; color: var(--green); line-height: 22px; }
  .product .btn { margin-top: 14px; width: 145px; height: 42px; }
  .referral {
    position: absolute; top: 1541px; left: 0; width: 600px; height: 300px;
    background: linear-gradient(90deg, #4a4a4c 0%, #38332f 35%, var(--lounge-wood) 70%, var(--lounge-dark) 100%);
  }
  .referral-copy {
    position: absolute; top: 74px; width: 100%;
    font-family: "Tinos", "Times New Roman", serif; font-weight: 700;
    font-size: 29px; line-height: 34px; color: var(--white);
  }
  .referral-copy em { font-style: normal; color: var(--red); }
  .btn-red {
    position: absolute; top: 188px; left: 194px; width: 211px; height: 36px;
    display: flex; align-items: center; justify-content: center;
    background: var(--red); color: var(--white); font-size: 15px; letter-spacing: 1.5px; text-decoration: none;
  }
  .contact-bar {
    position: absolute; top: 1841px; left: 0; width: 600px; height: 62px;
    background: var(--red); color: var(--white);
    display: flex; align-items: center; justify-content: center; font-size: 14px;
  }
  .contact-bar b { font-weight: 700; }
  .social { position: absolute; top: 1922px; width: 100%; display: flex; justify-content: center; gap: 14px; }
  .social span { width: 20px; height: 20px; border-radius: 50%; background: var(--social); }
  .footer { position: absolute; top: 1984px; left: 0; width: 600px; display: flex; }
  .footer-col { width: 300px; }
  .footer-col:first-child { width: 288px; }
  .footer-col h4 { font-size: 18px; font-weight: 500; color: var(--ink); line-height: 26px; }
  .footer-col address { margin-top: 16px; font-style: normal; font-size: 13px; line-height: 22px; color: var(--muted); }
</style>
</head>
<body>
<main class="email">
  <header class="masthead">
    <span class="brand-name">Vetrascan</span>
  </header>

  <section class="hero">
    <div role="img" aria-label="Bright white kitchen with subway tiles, range cooker and window herbs" style="position:absolute;inset:0"></div>
    <div class="hero-copy">
      <p class="hero-kicker">New Arrival Sale</p>
      <h1 class="hero-title">SALE</h1>
      <p class="hero-offer">UP TO <em>20%</em> OFF</p>
      <a class="btn" href="#">LEARN MORE</a>
    </div>
  </section>

  <section class="intro">
    <h2 class="section-title">New Arrival Devices</h2>
    <p>A long established fact that a reader will be distracted by the readable content of a page when looking at its layout. The point of using Lorem Ipsum is that it has a more-or-less normal distribution</p>
  </section>

  <section class="products">
    <article class="product">
      <div class="product-photo" role="img" aria-label="Modern kitchen with timber ceiling, dark cabinetry and white island"></div>
      <h3>Popular Devices</h3>
      <p>Lorem Ipsum is simply dummy text of the printing and typesetting industry. Lorem Ipsum has been the industry's standard dummy text ever since the 1500s</p>
      <div class="price">$699</div>
      <a class="btn" href="#">LEARN MORE</a>
    </article>
    <article class="product">
      <div class="product-photo" role="img" aria-label="Modern kitchen with timber ceiling, dark cabinetry and white island"></div>
      <h3>Popular Devices</h3>
      <p>Lorem Ipsum is simply dummy text of the printing and typesetting industry. Lorem Ipsum has been the industry's standard dummy text ever since the 1500s</p>
      <div class="price">$699</div>
      <a class="btn" href="#">LEARN MORE</a>
    </article>
    <article class="product">
      <div class="product-photo" role="img" aria-label="Modern kitchen with timber ceiling, dark cabinetry and white island"></div>
      <h3>New Arrival Devices</h3>
      <p>Lorem Ipsum is simply dummy text of the printing and typesetting industry. Lorem Ipsum has been the industry's standard dummy text ever since the 1500s</p>
      <div class="price">$699</div>
      <a class="btn" href="#">LEARN MORE</a>
    </article>
    <article class="product">
      <div class="product-photo" role="img" aria-label="Modern kitchen with timber ceiling, dark cabinetry and white island"></div>
      <h3>Popular Devices</h3>
      <p>Lorem Ipsum is simply dummy text of the printing and typesetting industry. Lorem Ipsum has been the industry's standard dummy text ever since the 1500s</p>
      <div class="price">$699</div>
      <a class="btn" href="#">LEARN MORE</a>
    </article>
  </section>

  <section class="referral">
    <div role="img" aria-label="Dark dining room with wood panelling, pendant lights and gold-framed chairs" style="position:absolute;inset:0"></div>
    <p class="referral-copy">Get <em>$1000/-</em> for every friend who uses<br>their $20 welcome offer</p>
    <a class="btn-red" href="#">Get Your Order Here!</a>
  </section>

  <div class="contact-bar">Contact us anytime at&nbsp;<b>+ 61 438 915 264</b>&nbsp;, or&nbsp;<b>Dean.orsk@vetrascan.com.au</b></div>

  <nav class="social" aria-label="Social links">
    <span></span><span></span><span></span><span></span><span></span>
  </nav>

  <footer class="footer">
    <div class="footer-col">
      <h4>Dean Orsk | Partner</h4>
      <address>Vetrascan Lifestyle Centre: Level 2,<br>Brackenfold Design Centre,<br>NSW 2043 Australia</address>
    </div>
    <div class="footer-col">
      <h4>Vetrascan Lifestyle Centre:</h4>
      <address>Vetrascan Lifestyle Centre: Level 2,<br>Brackenfold Design Centre,<br>NSW 2043 Australia</address>
    </div>
  </footer>
</main>
</body>
</html>
```